PowerPoint design MedoraVix

We need a PowerPoint set-up based upon our existing logo (see joint file)
Our company is operating in the health care and life science sector. We are mainly focussing on international business

Target Market(s)

International

Industry/Entity Type

health care and life sciences

Requirements
Must have
• Logos as added

```html
<!DOCTYPE html>
<html lang="en">
<head>
<meta charset="utf-8">
<title>MedoraVix – Presentation Set-up</title>
<link rel="stylesheet" href="https://fonts.googleapis.com/css2?family=Roboto:wght@500;700;900&family=Arimo:wght@400;700&display=swap">
<style>
:root{
  --stage:#9c9ca2;
  --navy:#0d4a86;
  --navy-deep:#0a3a6b;
  --blue:#1f78c8;
  --blue-light:#4aa8e6;
  --green:#6cbb2c;
  --green-light:#a6cf45;
  --grey:#8f9294;
  --ink:#3d3d3d;
  --white:#ffffff;
}
*{box-sizing:border-box;margin:0;padding:0}
html,body{width:1200px;height:708px;overflow:hidden}
body{background:radial-gradient(ellipse at 50% 45%,#b3b3b8 0%,var(--stage) 70%,#8d8d93 100%);position:relative;font-family:"Arimo",Arial,sans-serif;color:var(--ink)}
.defs{position:absolute;width:0;height:0}
.slide{position:absolute;width:372px;height:209px;background:var(--white);overflow:hidden;box-shadow:0 4px 8px rgba(0,0,0,.35)}
.col-1{left:18px}.col-2{left:419px}.col-3{left:810px}
.row-1{top:25px}.row-2{top:249px}.row-3{top:476px}
.layer{position:absolute;left:0;top:0;width:372px;height:209px}
.brand-mini{position:absolute;left:304px;top:9px;display:flex;align-items:center;gap:3px;color:var(--white);font:700 8.5px "Roboto",Arial,sans-serif}
.brand-mini .dot{width:10px;height:10px;border-radius:50%;border:1.4px solid var(--white)}
.headline{position:absolute;left:18px;top:18px;font:700 13px/1 "Roboto",Arial,sans-serif;color:var(--navy);white-space:nowrap}
.accent{color:var(--green)}
.lede{position:absolute;left:18px;top:38px;width:135px;font-size:6.4px;line-height:7.8px;color:#444}
.section-title{position:absolute;font:700 10px/1 "Roboto",Arial,sans-serif;color:var(--navy);white-space:nowrap}
.body-copy{position:absolute;font-size:6.9px;line-height:7.75px;color:#333}
.fine{position:absolute;font-size:4.5px;line-height:5.4px;color:#333}
.bullets{position:absolute;width:112px;list-style:none}
.bullets li{position:relative;padding-left:6px;font-size:4.5px;line-height:5.3px;color:#333;margin-bottom:5.8px}
.bullets li::before{content:"";position:absolute;left:0;top:1.2px;width:2.6px;height:2.6px;border-radius:50%;background:#555}
.option-title{position:absolute;font:500 10px/1 "Roboto",Arial,sans-serif;white-space:nowrap}
.option-title.blue{color:var(--blue)}
.option-title.green{color:var(--green)}
.option-title.grey{color:#666}
.cover-title{position:absolute;left:16px;top:67px;font:900 21px/21px "Roboto",Arial,sans-serif;color:var(--navy)}
.cover-title .accent{display:block;color:var(--green)}
.cover-brand{position:absolute;left:228px;top:163px;display:flex;align-items:center;gap:7px;font:700 17px "Roboto",Arial,sans-serif;color:var(--navy)}
.cover-brand .dot{width:28px;height:28px;border-radius:50%;border:3px solid var(--green)}
.closing{background:var(--navy)}
.closing-brand{position:absolute;left:72px;top:76px;display:flex;align-items:center;gap:16px;font:500 33px "Roboto",Arial,sans-serif;color:var(--white)}
.closing-brand .dot{width:56px;height:56px;border-radius:50%;border:4px solid var(--white)}
.center{text-align:center}
</style>
</head>
<body>

<svg class="defs" aria-hidden="true">
  <defs>
    <linearGradient id="blueBand" x1="0" y1="0" x2="0" y2="1">
      <stop offset="0" stop-color="#4ea9e8"/><stop offset="1" stop-color="#1a6fc0"/>
    </linearGradient>
    <linearGradient id="greenBand" x1="0" y1="0" x2="0" y2="1">
      <stop offset="0" stop-color="#67ad2a"/><stop offset="1" stop-color="#a9d046"/>
    </linearGradient>
    <linearGradient id="greenRow" x1="0" y1="0" x2="1" y2="0">
      <stop offset="0" stop-color="#6cb52c"/><stop offset="1" stop-color="#a9d046"/>
    </linearGradient>
    <linearGradient id="navyRow" x1="0" y1="0" x2="1" y2="0">
      <stop offset="0" stop-color="#0a3a6b"/><stop offset="1" stop-color="#155a99"/>
    </linearGradient>
    <linearGradient id="blueRow" x1="0" y1="0" x2="1" y2="0">
      <stop offset="0" stop-color="#1f78c8"/><stop offset="1" stop-color="#56b0ea"/>
    </linearGradient>
  </defs>
</svg>

<!-- Cover -->
<section class="slide col-1 row-1 cover">
  <svg class="layer" viewBox="0 0 372 209" aria-hidden="true">
    <polygon points="0,0 169,0 192,44 0,44" fill="url(#greenBand)"/>
    <polygon points="169,0 372,0 372,76 240,76" fill="url(#blueBand)"/>
    <polygon points="187,76 372,76 372,87 198,87" fill="var(--navy)"/>
  </svg>
  <h1 class="cover-title">TITLE<span class="accent">PRESENTATION</span></h1>
  <p class="lede" style="top:149px;left:17px">Lorem Ipsum is simply dummy text of the printing and typesetting industry.</p>
  <div class="cover-brand"><span class="dot"></span>MedoraVix</div>
</section>

<!-- Text slide -->
<section class="slide col-2 row-1">
  <svg class="layer" viewBox="0 0 372 209" aria-hidden="true">
    <polygon points="0,0 228,0 226,7 0,7" fill="var(--green-light)"/>
    <polygon points="240,0 372,0 372,32 297,32" fill="url(#blueBand)"/>
    <polygon points="297,32 372,32 372,40 305,40" fill="var(--navy)"/>
  </svg>
  <div class="brand-mini"><span class="dot"></span>MedoraVix</div>
  <h2 class="headline">HEADLINE TITLE <span class="accent">GOES HERE</span></h2>
  <p class="lede">Lorem Ipsum is simply dummy text of the printing and typesetting industry.</p>
  <h3 class="section-title" style="left:180px;top:83px">SECTION <span class="accent">TITLE</span></h3>
  <p class="body-copy" style="left:182px;top:94px;width:170px">Lorem Ipsum is simply dummy text of the printing and typesetting industry. Lorem Ipsum has been the industry's standard dummy text ever since the 1500s, when an unknown printer took a galley of type and scrambled it to make a type specimen.Lorem Ipsum is simply dummy text of the printing and typesetting industry. Lorem Ipsum has been the industry's standard dummy text ever since the 1500oy text of the printing and typesetting industry. Lorem Ipsum has been the industry's standard dummy text ever since the 1500s, when an unknown printer took a galley of type and scrambled it to make a type specimen.</p>
</section>

<!-- Two column bullets -->
<section class="slide col-3 row-1">
  <svg class="layer" viewBox="0 0 372 209" aria-hidden="true">
    <polygon points="0,0 228,0 226,7 0,7" fill="var(--green-light)"/>
    <polygon points="240,0 372,0 372,32 297,32" fill="url(#blueBand)"/>
    <polygon points="297,32 372,32 372,40 305,40" fill="var(--navy)"/>
  </svg>
  <div class="brand-mini"><span class="dot"></span>MedoraVix</div>
  <h2 class="headline">HEADLINE TITLE <span class="accent">GOES HERE</span></h2>
  <p class="lede">Lorem Ipsum is simply dummy text of the printing and typesetting industry.</p>
  <h3 class="section-title" style="left:23px;top:83px">SECTION <span class="accent">TITLE</span></h3>
  <ul class="bullets" style="left:23px;top:93px">
    <li>Lorem Ipsum is simply dummy text of the printing and typesetting industry. Lorem Ipsum has been the industry's standard dummy text ever since.</li>
    <li>Lorem Ipsum is simply dummy text of the printing and typesetting industry. Lorem Ipsum has been the industry's standard dummy text ever since.</li>
    <li>Lorem Ipsum is simply dummy text of the printing and typesetting industry. Lorem Ipsum has been the industry's standard dummy text ever since.</li>
    <li>Lorem Ipsum is simply dummy text of the printing and typesetting industry. Lorem Ipsum has been the industry's standard dummy text ever since.</li>
  </ul>
  <h3 class="section-title" style="left:207px;top:83px">SECTION <span class="accent">TITLE</span></h3>
  <ul class="bullets" style="left:207px;top:93px">
    <li>Lorem Ipsum is simply dummy text of the printing and typesetting industry. Lorem Ipsum has been the industry's standard dummy text ever since.</li>
    <li>Lorem Ipsum is simply dummy text of the printing and typesetting industry. Lorem Ipsum has been the industry's standard dummy text ever since.</li>
    <li>Lorem Ipsum is simply dummy text of the printing and typesetting industry. Lorem Ipsum has been the industry's standard dummy text ever since.</li>
    <li>Lorem Ipsum is simply dummy text of the printing and typesetting industry. Lorem Ipsum has been the industry's standard dummy text ever since.</li>
  </ul>
</section>

<!-- Donut options -->
<section class="slide col-1 row-2">
  <svg class="layer" viewBox="0 0 372 209" aria-hidden="true">
    <polygon points="0,0 228,0 226,7 0,7" fill="var(--green-light)"/>
    <polygon points="240,0 372,0 372,32 297,32" fill="url(#blueBand)"/>
    <polygon points="297,32 372,32 372,40 305,40" fill="var(--navy)"/>
    <g transform="rotate(-90 190 136)" fill="none">
      <circle cx="190" cy="136" r="45" stroke="var(--grey)" stroke-width="26" pathLength="100" stroke-dasharray="17 83"/>
      <circle cx="190" cy="136" r="42" stroke="var(--green)" stroke-width="24" pathLength="100" stroke-dasharray="0 17 23 60"/>
      <circle cx="190" cy="136" r="39" stroke="var(--navy)" stroke-width="20" pathLength="100" stroke-dasharray="0 40 20 40"/>
      <circle cx="190" cy="136" r="46" stroke="var(--blue)" stroke-width="34" pathLength="100" stroke-dasharray="0 60 40 0"/>
    </g>
    <circle cx="190" cy="136" r="27" fill="var(--white)"/>
    <g fill="#a3a6a8">
      <circle cx="182" cy="130" r="3.4"/><circle cx="190" cy="128" r="3.8"/><circle cx="198" cy="130" r="3.4"/>
      <path d="M176 141a6 5 0 0 1 12 0z"/><path d="M192 141a6 5 0 0 1 12 0z"/><path d="M183 142a7 6 0 0 1 14 0z"/>
    </g>
  </svg>
  <div class="brand-mini"><span class="dot"></span>MedoraVix</div>
  <h2 class="headline">HEADLINE TITLE <span class="accent">GOES HERE</span></h2>
  <p class="lede">Lorem Ipsum is simply dummy text of the printing and typesetting industry.</p>
  <h3 class="option-title blue" style="left:16px;top:78px">OPTION A</h3>
  <p class="fine" style="left:17px;top:89px;width:106px">Lorem Ipsum is simply dummy text of the printing and typesetting industry. Lorem Ipsum has been the industry's standard dummy text ever since the 1500s, when an unknown printer took a galley of type and scrambled it to make a type specimen.</p>
  <h3 class="option-title blue" style="left:16px;top:137px">OPTION B</h3>
  <p class="fine" style="left:17px;top:147px;width:106px">Lorem Ipsum is simply dummy text of the printing and typesetting industry. Lorem Ipsum has been the industry's standard dummy text ever since the 1500s, when an unknown printer took a galley of type and scrambled it to make a type specimen.</p>
  <h3 class="option-title green" style="left:255px;top:78px">OPTION A</h3>
  <p class="fine" style="left:256px;top:89px;width:106px">Lorem Ipsum is simply dummy text of the printing and typesetting industry. Lorem Ipsum has been the industry's standard dummy text ever since the 1500s, when an unknown printer took a galley of type and scrambled it to make a type specimen.</p>
  <h3 class="option-title grey" style="left:255px;top:137px">OPTION B</h3>
  <p class="fine" style="left:256px;top:147px;width:106px">Lorem Ipsum is simply dummy text of the printing and typesetting industry. Lorem Ipsum has been the industry's standard dummy text ever since the 1500s, when an unknown printer took a galley of type and scrambled it to make a type specimen.</p>
</section>

<!-- Phone infographic -->
<section class="slide col-2 row-2">
  <svg class="layer" viewBox="0 0 372 209" aria-hidden="true">
    <polygon points="0,0 228,0 226,7 0,7" fill="var(--green-light)"/>
    <polygon points="240,0 372,0 372,32 297,32" fill="url(#blueBand)"/>
    <polygon points="297,32 372,32 372,40 305,40" fill="var(--navy)"/>
    <!-- rows -->
    <polygon points="0,54 161,54 187,72 340,72 340,104 187,104 161,100 0,100" fill="url(#greenRow)"/>
    <polygon points="0,101 161,101 187,106 340,106 340,137 187,137 161,143 0,143" fill="url(#navyRow)"/>
    <polygon points="0,145 161,145 187,139 340,139 340,171 187,171 161,188 0,188" fill="url(#blueRow)"/>
    <!-- phone -->
    <rect x="277" y="58" width="66" height="132" rx="5" fill="#2b2b2e"/>
    <rect x="281" y="66" width="58" height="112" fill="none"/>
    <rect x="281" y="72" width="58" height="32" fill="#8cc63f"/>
    <rect x="281" y="106" width="58" height="31" fill="#134f8a"/>
    <rect x="281" y="139" width="58" height="32" fill="#3f9be0"/>
    <circle cx="310" cy="184" r="4" fill="none" stroke="#777" stroke-width="1"/>
    <!-- icons -->
    <g fill="var(--white)">
      <circle cx="310" cy="87" r="13"/><circle cx="310" cy="122" r="13"/><circle cx="310" cy="156" r="13"/>
    </g>
    <rect x="302" y="83" width="13" height="7" rx="1" fill="var(--green)"/><rect x="315" y="85" width="4" height="5" fill="var(--green)"/>
    <circle cx="305" cy="91" r="1.5" fill="var(--green)"/><circle cx="315" cy="91" r="1.5" fill="var(--green)"/>
    <path d="M304 117v5a4 4 0 0 0 8 0v-5M312 124h3v-3" fill="none" stroke="var(--navy)" stroke-width="1.4"/>
    <circle cx="316" cy="120" r="2" fill="none" stroke="var(--navy)" stroke-width="1.2"/>
    <rect x="303" y="150" width="5" height="12" rx="2.5" fill="var(--blue)"/>
    <rect x="309" y="150" width="5" height="12" rx="2.5" fill="var(--blue)" transform="rotate(-40 311 156)"/>
    <!-- arrows -->
    <g stroke="var(--white)" stroke-width="1" fill="var(--white)">
      <line x1="222" y1="88" x2="272" y2="88"/><polygon points="220,88 225,85.5 225,90.5"/>
      <line x1="222" y1="122" x2="272" y2="122"/><polygon points="220,122 225,119.5 225,124.5"/>
      <line x1="222" y1="155" x2="272" y2="155"/><polygon points="220,155 225,152.5 225,157.5"/>
    </g>
    <!-- letter badges -->
    <g fill="var(--white)">
      <circle cx="18" cy="75" r="8"/><circle cx="18" cy="121" r="8"/><circle cx="18" cy="168" r="8"/>
    </g>
    <g font-family="Roboto, Arial, sans-serif" font-weight="700" font-size="8" text-anchor="middle">
      <text x="18" y="78" fill="var(--green)">A</text>
      <text x="18" y="124" fill="var(--navy)">B</text>
      <text x="18" y="171" fill="var(--blue)">C</text>
    </g>
    <!-- text lines -->
    <g fill="var(--white)">
      <rect x="34" y="68" width="47" height="1.6"/><rect x="34" y="72" width="116" height="1"/><rect x="34" y="75" width="116" height="1"/><rect x="34" y="78" width="116" height="1"/><rect x="34" y="81" width="116" height="1"/>
      <rect x="34" y="114" width="47" height="1.6"/><rect x="34" y="118" width="116" height="1"/><rect x="34" y="121" width="116" height="1"/><rect x="34" y="124" width="116" height="1"/><rect x="34" y="127" width="116" height="1"/>
      <rect x="34" y="161" width="47" height="1.6"/><rect x="34" y="165" width="116" height="1"/><rect x="34" y="168" width="116" height="1"/><rect x="34" y="171" width="116" height="1"/><rect x="34" y="174" width="116" height="1"/>
    </g>
  </svg>
  <div class="brand-mini"><span class="dot"></span>MedoraVix</div>
  <h2 class="headline">HEADLINE TITLE <span class="accent">GOES HERE</span></h2>
  <p class="lede">Lorem Ipsum is simply dummy text of the printing and typesetting industry.</p>
</section>

<!-- Charts -->
<section class="slide col-3 row-2">
  <svg class="layer" viewBox="0 0 372 209" aria-hidden="true">
    <polygon points="0,0 228,0 226,7 0,7" fill="var(--green-light)"/>
    <polygon points="240,0 372,0 372,32 297,32" fill="url(#blueBand)"/>
    <polygon points="297,32 372,32 372,40 305,40" fill="var(--navy)"/>
    <!-- line / area chart -->
    <polygon points="27,185 45,172 62,158 80,142 92,128 104,140 116,148 128,135 138,130 150,145 150,185" fill="url(#greenBand)"/>
    <polyline points="27,184 45,168 62,145 76,150 92,132 104,140 118,126 128,104 138,116 150,130" fill="none" stroke="var(--blue-light)" stroke-width=".8"/>
    <polyline points="27,184 45,176 62,160 76,150 88,138 96,131 106,140 118,134 126,110 136,130 150,136" fill="none" stroke="var(--navy)" stroke-width=".8"/>
    <g stroke="#333" stroke-width=".5">
      <line x1="25" y1="111" x2="25" y2="186"/><line x1="24" y1="185" x2="151" y2="185"/>
    </g>
    <g fill="#555" font-size="2.2" font-family="Arimo, Arial, sans-serif">
      <text x="34" y="189">01</text><text x="48" y="189">02</text><text x="62" y="189">03</text><text x="76" y="189">04</text><text x="90" y="189">05</text><text x="104" y="189">06</text><text x="118" y="189">07</text><text x="132" y="189">08</text><text x="144" y="189">09</text>
    </g>
    <!-- jagged area chart -->
    <polygon points="226,137 234,132 240,126 246,124 252,116 256,110 260,104 264,92 268,110 272,102 276,98 280,108 284,96 288,104 292,100 296,112 300,96 304,106 308,104 312,92 316,108 320,104 324,110 328,98 332,112 336,118 340,122 346,137" fill="var(--green)"/>
    <polygon points="226,137 234,130 240,128 246,118 250,122 254,110 258,118 262,108 266,114 270,100 274,112 278,104 282,114 286,108 290,116 294,106 298,118 302,112 306,118 310,106 314,118 318,110 322,120 326,112 330,124 336,126 342,130 346,137" fill="var(--blue)"/>
    <polygon points="226,137 236,133 242,130 248,126 252,128 256,122 260,126 264,118 268,124 272,116 276,124 280,120 284,126 288,118 292,124 296,120 300,126 304,120 308,128 312,122 316,126 320,120 324,128 328,124 334,128 340,130 346,137" fill="var(--navy)"/>
    <g stroke="#333" stroke-width=".5">
      <line x1="225" y1="80" x2="225" y2="138"/><line x1="224" y1="137" x2="348" y2="137"/>
    </g>
    <g fill="#555" font-size="2.2" font-family="Arimo, Arial, sans-serif">
      <text x="232" y="141">01</text><text x="246" y="141">02</text><text x="260" y="141">03</text><text x="274" y="141">04</text><text x="288" y="141">05</text><text x="302" y="141">06</text><text x="316" y="141">07</text><text x="330" y="141">08</text><text x="342" y="141">09</text>
    </g>
  </svg>
  <div class="brand-mini"><span class="dot"></span>MedoraVix</div>
  <h2 class="headline">HEADLINE TITLE <span class="accent">GOES HERE</span></h2>
  <p class="lede">Lorem Ipsum is simply dummy text of the printing and typesetting industry.</p>
  <h3 class="section-title" style="left:17px;top:69px">SECTION <span class="accent">TITLE</span></h3>
  <p class="fine" style="left:17px;top:80px;width:140px">Lorem Ipsum is simply dummy text of the printing and typesetting industry. Lorem Ipsum has been the industry's standard dummy text ever since the 1500s, when an unknown printer took a galley of type and scrambled it to make a type specimen.</p>
  <h3 class="section-title" style="left:218px;top:69px">SECTION <span class="accent">TITLE</span></h3>
  <p class="fine" style="left:220px;top:158px;width:140px">Lorem Ipsum is simply dummy text of the printing and typesetting industry. Lorem Ipsum has been the industry's standard dummy text ever since the 1500s, when an unknown printer took a galley of type and scrambled it to make a type specimen.</p>
</section>

<!-- Timeline -->
<section class="slide col-1 row-3">
  <svg class="layer" viewBox="0 0 372 209" aria-hidden="true">
    <polygon points="0,0 228,0 226,7 0,7" fill="var(--green-light)"/>
    <polygon points="240,0 372,0 372,32 297,32" fill="url(#blueBand)"/>
    <polygon points="297,32 372,32 372,40 305,40" fill="var(--navy)"/>
    <polygon points="116,119 116,87 135,75 154,87 154,119" fill="url(#blueBand)"/>
    <polygon points="210,119 210,87 229,75 248,87 248,119" fill="url(#blueBand)"/>
    <polygon points="68,119 106,119 106,151 87,163 68,151" fill="url(#greenBand)"/>
    <polygon points="162,119 200,119 200,151 181,163 162,151" fill="url(#greenBand)"/>
    <polygon points="255,119 293,119 293,151 274,163 255,151" fill="url(#greenBand)"/>
    <line x1="43" y1="119" x2="319" y2="119" stroke="var(--navy)" stroke-width="3"/>
    <circle cx="43" cy="119" r="4.5" fill="var(--navy)"/><circle cx="319" cy="119" r="4.5" fill="var(--navy)"/>
    <g fill="none" stroke="var(--white)" stroke-width="1.5">
      <circle cx="135" cy="98" r="6"/><circle cx="229" cy="98" r="6"/>
      <circle cx="87" cy="139" r="6"/><circle cx="181" cy="139" r="6"/><circle cx="274" cy="139" r="6"/>
    </g>
  </svg>
  <div class="brand-mini"><span class="dot"></span>MedoraVix</div>
  <h2 class="headline">HEADLINE TITLE <span class="accent">GOES HERE</span></h2>
  <p class="lede">Lorem Ipsum is simply dummy text of the printing and typesetting industry.</p>
  <p class="fine center" style="left:100px;top:61px;width:76px">Lorem Ipsum is simply dummy text of the priindustry. Lorem Ipsum has.</p>
  <p class="fine center" style="left:194px;top:61px;width:76px">Lorem Ipsum is simply dummy text of the priindustry. Lorem Ipsum has.</p>
  <p class="fine center" style="left:50px;top:169px;width:76px">Lorem Ipsum is simply dummy text of the priindustry. Lorem Ipsum has.</p>
  <p class="fine center" style="left:143px;top:169px;width:76px">Lorem Ipsum is simply dummy text of the priindustry. Lorem Ipsum has.</p>
  <p class="fine center" style="left:236px;top:169px;width:76px">Lorem Ipsum is simply dummy text of the priindustry. Lorem Ipsum has.</p>
</section>

<!-- Section slide -->
<section class="slide col-2 row-3">
  <svg class="layer" viewBox="0 0 372 209" aria-hidden="true">
    <polygon points="0,0 204,0 154,52 0,52" fill="url(#greenBand)"/>
    <polygon points="204,126 372,126 372,144 187,144" fill="var(--navy)"/>
    <polygon points="187,144 372,144 372,209 115,209" fill="url(#blueBand)"/>
  </svg>
  <h3 class="section-title" style="left:12px;top:71px">SECTION <span class="accent">TITLE</span></h3>
  <p class="body-copy" style="left:14px;top:82px;width:140px">Lorem Ipsum is simply dummy text of the printing and typesetting industry. Lorem Ipsum has been the industry's standard dummy text ever since the 1500s, when an unknown printer took a galley of type and scrambled it to make a type specimen.Lorem Ipsum is simply dummy tesince the 1500oy text of the printing and typesetting industry. Lorem Ipsum has been the industry's standard dummy text ever since the 1500s, when an unknown printer took a galley of type and scrambled it to make a type specimen.</p>
  <p class="fine" style="left:14px;top:187px;width:120px;font-size:3.4px;line-height:4.4px;color:#555">Lorem ipsum dolor sit amet, consectetuer adipiscing elit, sed diam nonummy nibh euismod tincidunt.</p>
</section>

<!-- Closing -->
<section class="slide col-3 row-3 closing">
  <div class="closing-brand"><span class="dot"></span>MedoraVix</div>
</section>

</body>
</html>
```